Business Card Design

I am a Special Event Consultant,I arrange and organise Special Events - Product Launches,Sponsorship and Product Displays.

I would like the TRV to be a feature of the design with 'Special Event Services" underneath - keep it very simple but creative using this information. So it is just the letters "TRV" with Event Services underneath.

(Simple Colours - Silver, Black, Grey - no bright colours - We work for Valdoren Kraft,QJX, Tavrelli So it is class and classic.)

Only my Name and mobile on the front.

Industry/Entity Type

Business

Contact Information for Business Card

FRONT
Jo Pettigrew
Tel: 0427 318906

BACK
Email: jo@trvoccasionhire.com.au

1208 Wexley Court,72 Ormond Lane
KELMSTON.Vic.3145.

```html
<!DOCTYPE html>
<html lang="en">
<head>
<meta charset="utf-8">
<title>Jo Pettigrew — Business Card Concepts</title>
<link rel="stylesheet" href="https://fonts.googleapis.com/css2?family=Source+Sans+3:wght@400;600;700&family=Jost:wght@400;500&family=Arimo:wght@400;700&family=Questrial&display=swap">
<style>
  :root {
    --paper: #ffffff;
    --ink: #1a1a1a;
    --ink-soft: #3a3a3a;
    --grey: #8a8a8a;
    --grey-mid: #7f7f7f;
    --grey-light: #c4c4c4;
    --rule: #b5b5b5;
    --shadow: rgba(0, 0, 0, 0.28);
  }
  * { margin: 0; padding: 0; box-sizing: border-box; }
  html, body { width: 1200px; height: 900px; overflow: hidden; background: var(--paper); }
  .sheet { position: relative; width: 1200px; height: 900px; }
  .card {
    position: absolute;
    background: var(--paper);
    box-shadow: 2px 4px 7px var(--shadow);
    overflow: hidden;
    font-family: "Source Sans 3", sans-serif;
    color: var(--ink);
  }
  .t { position: absolute; white-space: nowrap; line-height: 1; }
  .centered { left: 0; right: 0; text-align: center; }

  /* Row one */
  .front-classic { left: 27px; top: 26px; width: 291px; height: 166px; }
  .front-classic .name { top: 93px; font-weight: 700; font-size: 19px; }
  .front-classic .tel { top: 124px; font-size: 10.5px; }

  .front-geometric { left: 379px; top: 26px; width: 290px; height: 166px; font-family: "Jost", sans-serif; }
  .front-geometric .name { top: 62px; font-weight: 500; font-size: 19px; }
  .front-geometric .tel { top: 143px; font-size: 11px; color: var(--ink-soft); }

  .front-tall { left: 769px; top: 34px; width: 166px; height: 290px; }
  .front-tall .name { top: 40px; font-weight: 700; font-size: 16.5px; }
  .front-tall .tel { top: 72px; font-size: 7px; color: var(--grey); font-weight: 600; }

  .front-circle { left: 993px; top: 38px; width: 166px; height: 286px; }
  .front-circle .badge { position: absolute; left: 20px; top: 57px; width: 126px; height: 126px; }
  .front-circle .badge-name {
    top: 113px; font-family: "Jost", sans-serif; font-size: 13px; color: var(--paper);
  }
  .front-circle .tel { top: 258px; font-size: 7px; color: var(--grey); font-weight: 600; }

  /* Row two */
  .back-classic { left: 27px; top: 245px; width: 291px; height: 165px; }
  .back-classic .email { left: 15px; top: 116px; font-size: 10px; }
  .back-classic .addr { left: 15px; top: 141px; font-size: 5.5px; line-height: 1.25; color: var(--ink-soft); }

  .back-ruled { left: 385px; top: 262px; width: 290px; height: 166px; }
  .back-ruled .rule { position: absolute; left: 0; right: 0; top: 113px; height: 1px; background: var(--rule); }
  .back-ruled .email { left: 13px; top: 120px; font-size: 10px; }
  .back-ruled .addr { left: 11px; top: 140px; font-size: 5.5px; line-height: 1.25; color: var(--ink-soft); }

  .back-tall { left: 769px; top: 354px; width: 166px; height: 291px; font-family: "Questrial", sans-serif; }
  .back-tall .addr { left: 12px; top: 228px; font-size: 6.5px; line-height: 1.35; color: var(--ink-soft); font-weight: 700; }
  .back-tall .email { left: 12px; top: 264px; font-size: 6.5px; color: var(--grey); }

  .back-tall-centered { left: 993px; top: 343px; width: 166px; height: 289px; font-family: "Questrial", sans-serif; }
  .back-tall-centered .email { top: 219px; font-size: 6.5px; color: var(--grey-mid); }
  .back-tall-centered .addr { top: 236px; font-size: 6.5px; line-height: 1.35; color: var(--grey-mid); }

  /* Row three */
  .front-band { left: 27px; top: 473px; width: 291px; height: 165px; font-family: "Arimo", sans-serif; }
  .front-band .name { left: 14px; top: 16px; font-weight: 700; font-size: 17px; color: var(--grey); }
  .front-band .tel { left: 35px; top: 40px; font-size: 10px; color: var(--grey); }
  .front-band .band { position: absolute; left: 0; right: 0; bottom: 0; height: 12px; background: var(--grey-mid); }

  .front-bold { left: 385px; top: 466px; width: 290px; height: 166px; font-family: "Arimo", sans-serif; }
  .front-bold .name { left: 13px; top: 104px; font-weight: 700; font-size: 18.5px; }
  .front-bold .tel { left: 13px; top: 125px; font-size: 9px; color: var(--grey-light); }

  /* Row four */
  .back-underlined { left: 27px; top: 701px; width: 291px; height: 165px; }
  .back-underlined .addr { left: 15px; top: 113px; font-size: 8px; line-height: 1.25; }
  .back-underlined .rule { position: absolute; left: 15px; width: 261px; top: 138px; height: 1px; background: var(--rule); }
  .back-underlined .email { left: 15px; top: 151px; font-size: 5.5px; color: var(--ink-soft); }

  .back-split { left: 385px; top: 693px; width: 290px; height: 165px; font-family: "Questrial", sans-serif; }
  .back-split .email { left: 12px; top: 149px; font-size: 6.5px; color: var(--grey-mid); }
  .back-split .addr { right: 5px; top: 139px; font-size: 6.5px; line-height: 1.35; color: var(--grey-mid); font-weight: 700; }

  .combined { left: 780px; top: 693px; width: 290px; height: 165px; font-family: "Questrial", sans-serif; }
  .combined .name { left: 16px; top: 20px; font-size: 16.5px; color: var(--grey-light); font-weight: 700; }
  .combined .tel { left: 15px; top: 135px; font-size: 6.5px; color: var(--grey-mid); }
  .combined .email { left: 15px; top: 149px; font-size: 6.5px; color: var(--grey-mid); }
  .combined .addr { right: 6px; top: 139px; font-size: 6.5px; line-height: 1.35; color: var(--grey-mid); }
</style>
</head>
<body>
<main class="sheet">

  <section class="card front-classic">
    <p class="t centered name">Jo Pettigrew</p>
    <p class="t centered tel">Tel: 0427 318906</p>
  </section>

  <section class="card front-geometric">
    <p class="t centered name">Jo Pettigrew</p>
    <p class="t centered tel">Tel: 0427 318906</p>
  </section>

  <section class="card front-tall">
    <p class="t centered name">Jo Pettigrew</p>
    <p class="t centered tel">Tel: 0427 318906</p>
  </section>

  <section class="card front-circle">
    <svg class="badge" viewBox="0 0 126 126" aria-hidden="true">
      <circle cx="63" cy="63" r="63" fill="#000"/>
    </svg>
    <p class="t centered badge-name">Jo Pettigrew</p>
    <p class="t centered tel">Tel: 0427 318906</p>
  </section>

  <section class="card back-classic">
    <p class="t email">jo@trvoccasionhire.com.au</p>
    <p class="t addr">1208 Wexley Court,72<br>Ormond Lane KELMSTON.Vic.3145</p>
  </section>

  <section class="card back-ruled">
    <div class="rule"></div>
    <p class="t email">jo@trvoccasionhire.com.au</p>
    <p class="t addr">1208 Wexley Court,72<br>Ormond Lane KELMSTON.Vic.3145</p>
  </section>

  <section class="card back-tall">
    <p class="t addr">1208 Wexley Court,72<br>Ormond Lane KELMSTON.Vic.3145</p>
    <p class="t email">jo@trvoccasionhire.com.au</p>
  </section>

  <section class="card back-tall-centered">
    <p class="t centered email">jo@trvoccasionhire.com.au</p>
    <p class="t centered addr">1208 Wexley Court,72<br>Ormond Lane KELMSTON.Vic.3145</p>
  </section>

  <section class="card front-band">
    <p class="t name">Jo Pettigrew</p>
    <p class="t tel">Tel: 0427 318906</p>
    <div class="band"></div>
  </section>

  <section class="card front-bold">
    <p class="t name">Jo Pettigrew</p>
    <p class="t tel">Tel: 0427 318906</p>
  </section>

  <section class="card back-underlined">
    <p class="t addr">1208 Wexley Court,72<br>Ormond Lane KELMSTON.Vic.3145</p>
    <div class="rule"></div>
    <p class="t email">jo@trvoccasionhire.com.au</p>
  </section>

  <section class="card back-split">
    <p class="t email">jo@trvoccasionhire.com.au</p>
    <p class="t addr">1208 Wexley Court,72<br>Ormond Lane KELMSTON.Vic.3145</p>
  </section>

  <section class="card combined">
    <p class="t name">Jo Pettigrew</p>
    <p class="t tel">Tel: 0427 318906</p>
    <p class="t email">jo@trvoccasionhire.com.au</p>
    <p class="t addr">1208 Wexley Court,72<br>Ormond Lane KELMSTON.Vic.3145</p>
  </section>

</main>
</body>
</html>
```